Business Card Design Project

2 sided business card utilizing existing logo
- English on one side, Arabic on the other side (both English and Arabic text will be provided)
Same color scheme as logo
Information included will be: name, title, email, phone, address and website (www.dravelnix.com)
Updates

Target Market(s)

We are a Systems Integration Company

Industry/Entity Type

Business

Font styles to use
Serif
Sans Serif

Requirements
Should not have
• We prefer using the flat logo rather than one with shadow/3D effect

```html
<!DOCTYPE html>
<html lang="en">
<head>
<meta charset="utf-8">
<title>Business card – font options</title>
<link rel="stylesheet" href="https://fonts.googleapis.com/css2?family=Fira+Sans:wght@300;400;500;600&family=Lato:wght@400;700&family=Raleway:wght@300&display=swap">
<style>
  :root {
    --board: #808080;
    --card-red: #e8262a;
    --ink: #ffffff;
  }
  * { margin: 0; padding: 0; box-sizing: border-box; }
  html, body { width: 1200px; height: 900px; overflow: hidden; background: var(--board); }
  .board { position: relative; width: 1200px; height: 900px; background: var(--board); color: var(--ink); font-family: "Fira Sans", sans-serif; }
  .board-title { position: absolute; left: 72px; top: 110px; font-size: 38px; font-weight: 300; letter-spacing: 0.3px; }
  .option { position: absolute; top: 205px; width: 284px; }
  .option--1 { left: 72px; }
  .option--2 { left: 458px; }
  .option--3 { left: 844px; }
  .option-label { position: absolute; top: 512px; left: 0; width: 284px; text-align: center; font-size: 38px; font-weight: 300; }

  .card {
    position: relative; width: 284px; height: 482px; background: var(--card-red);
    clip-path: polygon(0 0, 236px 0, 284px 48px, 284px 100%, 48px 100%, 0 434px);
    font-family: "Fira Sans", sans-serif; text-align: right;
  }
  .card--lato .card-details { font-family: "Lato", sans-serif; }
  .card > div { position: absolute; right: 32px; left: 10px; }
  .brand-name { top: 158px; font-size: 20px; font-weight: 600; letter-spacing: 5px; line-height: 22px; margin-right: -5px; }
  .person-name { top: 211px; font-size: 38px; line-height: 36px; }
  .card--1 .person-name { font-family: "Raleway", sans-serif; font-weight: 300; text-transform: uppercase; font-size: 37px; }
  .card--2 .person-name { font-weight: 300; }
  .card--3 .person-name { font-weight: 500; font-size: 40px; line-height: 39px; top: 212px; }
  .job-title { top: 284px; font-size: 13px; line-height: 16px; }
  .address { top: 318px; font-size: 13px; line-height: 17.5px; }
  .contacts { top: 366px; font-size: 13px; line-height: 19.5px; }
  .website { top: 440px; font-size: 13px; line-height: 16px; }
  .card--2 .card-details, .card--2 .job-title { font-size: 15px; }
  .card--3 .job-title { top: 291px; }
  .card--3 .address { top: 321px; line-height: 18.5px; }
  .card--3 .contacts { top: 371px; line-height: 18.5px; }
  .card--3 .website { top: 441px; }
  .contact-line { display: flex; justify-content: flex-end; align-items: center; gap: 5px; }
  .icon { width: 15px; height: 12px; fill: var(--ink); flex: none; }
</style>
</head>
<body>
<main class="board">
  <h1 class="board-title">font options:</h1>

  <section class="option option--1">
    <div class="card card--1 card--lato">
      <div class="brand-name">DRAVELNIX</div>
      <div class="person-name">Marcus<br>Feldane</div>
      <div class="job-title card-details">Creative Director</div>
      <div class="address card-details">27 Harlow Street<br>Fenwick, Ohio, 43120</div>
      <div class="contacts card-details">
        <p class="contact-line"><svg class="icon" viewBox="0 0 16 12"><path d="M1 4c0-2 3-3 7-3s7 1 7 3v1h-4V3.5H5V5H1z"/><path d="M3 6h10v5H3z"/></svg>+001 555 0142 318</p>
        <p class="contact-line"><svg class="icon" viewBox="0 0 16 12"><path d="M5 1h6v11H5z"/><path d="M6 2.5h4v3H6z" fill="#e8262a"/></svg>+001 555 0187 264</p>
        <p class="contact-line"><svg class="icon" viewBox="0 0 16 12"><path d="M1 1h14v10H1z M2.5 2.5v7h11v-7L8 7z" fill-rule="evenodd"/></svg>marcus@dravelnix.com</p>
      </div>
      <div class="website card-details">www.dravelnix.com</div>
    </div>
    <p class="option-label">option 1</p>
  </section>

  <section class="option option--2">
    <div class="card card--2">
      <div class="brand-name">DRAVELNIX</div>
      <div class="person-name">Marcus<br>Feldane</div>
      <div class="job-title card-details">Creative Director</div>
      <div class="address card-details">27 Harlow Street<br>Fenwick, Ohio, 43120</div>
      <div class="contacts card-details">
        <p class="contact-line"><svg class="icon" viewBox="0 0 16 12"><path d="M1 4c0-2 3-3 7-3s7 1 7 3v1h-4V3.5H5V5H1z"/><path d="M3 6h10v5H3z"/></svg>+001 555 0142 318</p>
        <p class="contact-line"><svg class="icon" viewBox="0 0 16 12"><path d="M5 1h6v11H5z"/><path d="M6 2.5h4v3H6z" fill="#e8262a"/></svg>+001 555 0187 264</p>
        <p class="contact-line"><svg class="icon" viewBox="0 0 16 12"><path d="M1 1h14v10H1z M2.5 2.5v7h11v-7L8 7z" fill-rule="evenodd"/></svg>marcus@dravelnix.com</p>
      </div>
      <div class="website card-details">www.dravelnix.com</div>
    </div>
    <p class="option-label">option 2</p>
  </section>

  <section class="option option--3">
    <div class="card card--3">
      <div class="brand-name">DRAVELNIX</div>
      <div class="person-name">Marcus<br>Feldane</div>
      <div class="job-title card-details">Creative Director</div>
      <div class="address card-details">27 Harlow Street<br>Fenwick, Ohio, 43120</div>
      <div class="contacts card-details">
        <p class="contact-line"><svg class="icon" viewBox="0 0 16 12"><path d="M1 4c0-2 3-3 7-3s7 1 7 3v1h-4V3.5H5V5H1z"/><path d="M3 6h10v5H3z"/></svg>+001 555 0142 318</p>
        <p class="contact-line"><svg class="icon" viewBox="0 0 16 12"><path d="M5 1h6v11H5z"/><path d="M6 2.5h4v3H6z" fill="#e8262a"/></svg>+001 555 0187 264</p>
        <p class="contact-line"><svg class="icon" viewBox="0 0 16 12"><path d="M1 1h14v10H1z M2.5 2.5v7h11v-7L8 7z" fill-rule="evenodd"/></svg>marcus@dravelnix.com</p>
      </div>
      <div class="website card-details">www.dravelnix.com</div>
    </div>
    <p class="option-label">option 3</p>
  </section>
</main>
</body>
</html>
```